Business Card for Brivanta Web
Brivanta Web
Project: Business Card for Brivanta Web
Business Card for Brivanta Web - Information Technology
Creative Brief
Professional
Dana Holbrook
7312 Ferncliff Drive #210 Harlow Ridge, NC 28099
919-555-0164 ext. 214
dana.holbrook@brivanta.example
www.brivanta.example
Please incorporate uploaded logo in your design
Logo + Brivanta Web or designs' ideas

```html
<!DOCTYPE html>
<html lang="en">
<head>
<meta charset="utf-8">
<title>Brivanta Web – Business Card</title>
<link href="https://fonts.googleapis.com/css2?family=Open+Sans:wght@400;600;700&display=swap" rel="stylesheet">
<style>
  :root{
    --page:#e9eaec;
    --card:#ffffff;
    --brand-blue:#2b3f9e;
    --steel:#5a6b8c;
    --ink:#3c3f45;
    --line-grey:#b9bcc1;
    --black:#111216;
  }
  *{margin:0;padding:0;box-sizing:border-box}
  html,body{width:1200px;height:864px;overflow:hidden}
  body{
    background:var(--page);
    font-family:"Open Sans",Arial,sans-serif;
    display:flex;flex-direction:column;align-items:center;justify-content:center;gap:48px;
  }
  .card{
    position:relative;width:630px;height:360px;background:var(--card);
    border-radius:22px;overflow:hidden;
    box-shadow:0 6px 18px rgba(0,0,0,.12);
  }
  /* front */
  .card-front{display:flex;flex-direction:column;align-items:center;justify-content:center;gap:26px}
  .brand{display:flex;align-items:center;gap:14px}
  .brand-dot{width:70px;height:70px;border-radius:50%;background:var(--steel)}
  .brand-name{font-weight:700;color:var(--brand-blue);font-size:34px;letter-spacing:.5px;white-space:nowrap}
  .site{font-size:12px;letter-spacing:5px;color:var(--brand-blue);text-transform:lowercase}
  /* back */
  .card-back .brand{position:absolute;left:54px;top:66px;gap:10px}
  .card-back .brand-dot{width:46px;height:46px}
  .card-back .brand-name{font-size:24px}
  .person{position:absolute;left:58px;top:150px}
  .person-name{color:var(--brand-blue);font-size:16px;font-weight:600;margin-bottom:10px}
  .address{color:var(--ink);font-size:12px;line-height:1.55}
  .contacts{position:absolute;left:318px;top:60px;list-style:none;border-left:1px solid var(--line-grey);padding-left:14px}
  .contacts li{display:flex;align-items:center;gap:8px;font-size:12px;color:var(--ink);line-height:21px;white-space:nowrap}
  .contact-icon{width:13px;height:13px;border-radius:50%;background:var(--brand-blue);flex:none;display:flex;align-items:center;justify-content:center}
  .contact-icon svg{width:8px;height:8px}
  .swoosh{position:absolute;left:0;bottom:0;width:630px;height:130px}
</style>
</head>
<body>
  <section class="card card-front">
    <div class="brand">
      <span class="brand-dot"></span>
      <span class="brand-name">Brivanta Web</span>
    </div>
    <p class="site">www.brivanta.example</p>
  </section>

  <section class="card card-back">
    <div class="brand">
      <span class="brand-dot"></span>
      <span class="brand-name">Brivanta Web</span>
    </div>
    <div class="person">
      <p class="person-name">Dana Holbrook</p>
      <p class="address">7312 Ferncliff Drive #210<br>Harlow Ridge, NC 28099</p>
    </div>
    <ul class="contacts">
      <li><span class="contact-icon"><svg viewBox="0 0 8 8"><path d="M1 1h2l1 2-1 1a4 4 0 0 0 1 1l1-1 2 1v2C4 7 1 4 1 1z" fill="#fff"/></svg></span>1-866-555-0142</li>
      <li><span class="contact-icon"><svg viewBox="0 0 8 8"><path d="M1 1h2l1 2-1 1a4 4 0 0 0 1 1l1-1 2 1v2C4 7 1 4 1 1z" fill="#fff"/></svg></span>919-555-0164 ext. 214</li>
      <li><span class="contact-icon"><svg viewBox="0 0 8 8"><rect x="1.5" y="2" width="5" height="4" fill="#fff"/></svg></span>919-555-0187</li>
      <li><span class="contact-icon"><svg viewBox="0 0 8 8"><path d="M1 2h6v4H1z M1 2l3 2 3-2" fill="none" stroke="#fff" stroke-width="1"/></svg></span>dana.holbrook@brivanta.example</li>
      <li><span class="contact-icon"><svg viewBox="0 0 8 8"><circle cx="4" cy="4" r="2.6" fill="none" stroke="#fff" stroke-width="1"/></svg></span>www.brivanta.example</li>
    </ul>
    <svg class="swoosh" viewBox="0 0 630 130" preserveAspectRatio="none" aria-hidden="true">
      <defs>
        <linearGradient id="blueWave" x1="0" y1="0" x2="1" y2="0">
          <stop offset="0" stop-color="#3f56c4"/>
          <stop offset="1" stop-color="#1b2a78"/>
        </linearGradient>
      </defs>
      <path d="M0 112 C180 112 330 40 630 14 L630 130 L0 130Z" fill="var(--line-grey)"/>
      <path d="M0 118 C190 118 340 52 630 30 L630 130 L0 130Z" fill="var(--black)"/>
      <path d="M0 124 C200 124 350 66 630 46 L630 130 L0 130Z" fill="url(#blueWave)"/>
    </svg>
  </section>
</body>
</html>
```